CoverLantern.com website re-design - modern engaging website creation

We have an existing website. Www.CoverLantern.com - the content on the site and our widgets are custom built. But the layout and design of our site we just put there as we built the functionality around it. We want a new, bold, and modern design aimed at getting visitors to run a life insurance quote and ultimately apply. Our demographic is centered around those between the ages of 30-60. So we are looking at a complete site overhaul with better pictures, buttons, and an extremely modern design.

Target Market(s)

30-50 year olds

Industry/Entity Type

Life insurance

Coding

Coded - Design and coding required

Number of Pages Required

5+ page

Font styles to use
Other font styles liked:
• Rubik

Colors
0054AA
0677BA
7BADD7
CADEEF
E8F1F8
00AB8E
00BBA5
67D7C9
C6EFE9
E9F9F6
59FF00
82FF00
B8FF75
E3FFCB
F4FFEA

Requirements
Must have
• Matching color schemes from existing website. We have custom widgets on our site now and those must be . White space is important to make it simple for the user to navigate
Nice to have
• Same content - different more modern design
Should not have
• Colors outside of our current color scheme. Should NOT be too similar to our existing site.

```html
<!DOCTYPE html>
<html lang="en">
<head>
<meta charset="utf-8">
<title>CoverLantern – Term Life Insurance</title>
<link href="https://fonts.googleapis.com/css2?family=Rubik:wght@400;500;600;700&display=swap" rel="stylesheet">
<style>
:root{
  --blue:#0054AA;
  --blue-mid:#0677BA;
  --blue-soft:#7BADD7;
  --blue-pale:#CADEEF;
  --blue-mist:#E8F1F8;
  --teal:#00AB8E;
  --teal-pale:#C6EFE9;
  --green:#8BC53F;
  --green-light:#B8E07A;
  --green-pale:#E3F5CB;
  --ink:#222;
  --muted:#666;
  --white:#fff;
}
*{margin:0;padding:0;box-sizing:border-box}
html,body{width:1200px;height:4441px;overflow:hidden;background:var(--white)}
body{font-family:"Rubik",sans-serif;color:var(--ink)}
.page{position:relative;width:1200px;height:4441px;overflow:hidden}
.abs{position:absolute}
.btn{position:absolute;display:flex;align-items:center;justify-content:center;background:var(--green);color:var(--white);font-weight:600;font-size:14px;letter-spacing:.3px;border-radius:22px;height:36px;text-transform:uppercase}
.btn--blue{background:var(--blue-mid)}

/* top bar & header */
.topbar{left:0;top:0;width:1200px;height:34px;background:var(--blue)}
.topbar__app{right:298px;top:10px;color:var(--white);font-size:11px;display:flex;gap:8px;align-items:center}
.topbar__login{right:60px;top:0;width:220px;height:34px;background:var(--green);color:var(--white);font-size:13px;font-weight:600;display:flex;align-items:center;justify-content:center;gap:8px}
.header{left:0;top:34px;width:1200px;height:66px;background:var(--white)}
.brand{font-size:32px;font-weight:400;color:var(--blue)}
.header .brand{left:58px;top:10px}
.nav{right:62px;top:28px;display:flex;gap:24px;font-size:11.5px;color:#333;font-weight:500}

/* hero */
.hero-photo{left:0;top:100px;width:1200px;height:600px;background:linear-gradient(110deg,#5a6670 0%,#7d7770 35%,#9a8a7c 60%,#b7a99a 100%)}
.hero-shade{left:0;top:100px;width:700px;height:600px;background:linear-gradient(90deg,rgba(30,40,60,.55),rgba(30,40,60,0))}
.hero__title{left:60px;top:236px;color:var(--white);font-size:70px;font-weight:600;line-height:64px}
.hero__sub{left:62px;top:384px;color:var(--white);font-size:14px}
.hero__dots{left:1130px;top:280px;display:flex;flex-direction:column;gap:14px}
.hero__dots span{width:9px;height:9px;border-radius:50%;background:var(--green)}
.hero__dots span.on{background:var(--white)}

/* content sections */
.h2{font-size:30px;font-weight:500;color:var(--blue-mid)}
.lede{font-size:11.5px;color:var(--muted);line-height:19px}
.points{list-style:none;font-size:11.5px;color:var(--muted);line-height:19px}
.points li{position:relative;padding-left:24px;margin-bottom:14px}
.points li::before{content:"";position:absolute;left:2px;top:4px;width:2px;height:12px;background:var(--green);transform:rotate(20deg)}
.points li.strong{font-size:14px;color:#333}

.arch{border-radius:200px 200px 0 0;overflow:hidden;border:8px solid var(--white);box-shadow:0 0 18px rgba(0,0,0,.08)}
.circle{border-radius:50%;border:8px solid var(--white);box-shadow:0 0 18px rgba(0,0,0,.08)}

.carrier-panel{left:617px;top:828px;width:314px;height:206px;background:var(--teal-pale);border-radius:10px}
.carrier-panel__bar{height:22px;background:var(--teal);border-radius:10px 10px 0 0;display:flex;gap:6px;align-items:center;padding-left:12px}
.carrier-panel__bar i{width:7px;height:7px;border-radius:50%;background:var(--white)}
.carrier-grid{display:grid;grid-template-columns:repeat(3,88px);gap:10px;padding:16px 18px}
.carrier{height:68px;background:var(--white);border-radius:6px;display:flex;align-items:center;justify-content:center;font-size:13px;font-weight:500;color:var(--blue);text-align:center}

.quote-card{position:absolute;width:225px;height:88px;border-radius:8px;padding:14px 12px 0 72px;font-size:10px;font-weight:500;color:#333;line-height:14px}
.quote-card .seal{position:absolute;left:16px;top:18px;width:44px;height:44px;border-radius:50%;background:var(--white)}
.quote-card .price{font-size:20px;font-weight:600;color:var(--teal);margin-top:6px}
.quote-card .price small{font-size:9px;color:#555}

.contact-line{display:flex;gap:14px;align-items:center;font-size:14px;color:#333}
.contact-line b{font-weight:600}

/* partners */
.partners__title{left:0;top:3640px;width:1200px;text-align:center;font-size:28px;font-weight:600;color:var(--blue-mid)}
.partner{position:absolute;width:200px;height:100px;display:flex;align-items:center;justify-content:center;font-size:24px;font-weight:600;color:var(--blue)}

/* footer */
.footer-col h4{font-size:15px;font-weight:500;color:var(--white);margin-bottom:18px}
.footer-col ul{list-style:none;font-size:11px;color:var(--white);line-height:24px}
.footer-col li{padding-left:18px;position:relative}
.footer-col li::before{content:"";position:absolute;left:0;top:10px;width:5px;height:5px;border-radius:50%;background:var(--green)}
.footer-contact{font-size:11px;color:var(--white);line-height:16px}
.footer-contact div{display:flex;gap:16px;margin-bottom:14px}
.social{display:flex;gap:8px}
.social span{width:32px;height:32px;border-radius:50%;background:var(--green)}
.copyright{left:0;top:4412px;width:1200px;text-align:center;font-size:10.5px;color:var(--white)}
</style>
</head>
<body>
<div class="page">

  <!-- top bar -->
  <div class="abs topbar"></div>
  <div class="abs topbar__app">
    <svg width="12" height="16" viewBox="0 0 12 16"><rect x="1" y="1" width="10" height="14" rx="2" fill="none" stroke="#fff" stroke-width="1.4"/></svg>
    CONTINUE APPLICATION
  </div>
  <div class="abs topbar__login">
    <svg width="16" height="16" viewBox="0 0 16 16"><circle cx="8" cy="8" r="7" fill="none" stroke="#fff" stroke-width="1.4"/><circle cx="8" cy="6.5" r="2.4" fill="#fff"/></svg>
    EXISTING CLIENT LOGIN
  </div>
  <div class="abs header">
    <div class="abs brand">CoverLantern</div>
    <nav class="abs nav"><span>FREE QUOTE</span><span>NO EXAM</span><span>ARTICLES</span><span>FAQ'S</span><span>ABOUT</span><span>CONTACT</span></nav>
  </div>

  <!-- hero -->
  <div class="abs hero-photo" role="img" aria-label="Photo of a father and child relaxing together on a sofa with a laptop"></div>
  <div class="abs hero-shade"></div>
  <h1 class="abs hero__title">Term Life<br>Insurance</h1>
  <p class="abs hero__sub">Purchase Life Insurance Online | Quote Yourself | Apply In Minutes</p>
  <div class="btn" style="left:60px;top:420px;width:209px">Get Your Quote Now</div>
  <div class="abs hero__dots"><span></span><span class="on"></span><span></span></div>
  <svg class="abs" style="left:0;top:560px" width="1200" height="160" viewBox="0 0 1200 160">
    <path d="M0 70 C250 140 500 150 760 80 C900 40 1050 20 1200 40 L1200 160 L0 160 Z" fill="var(--green)"/>
    <path d="M0 110 C260 160 520 150 780 100 C930 70 1060 60 1200 80 L1200 160 L0 160 Z" fill="var(--white)"/>
    <path d="M700 70 C860 20 1040 20 1145 105" fill="none" stroke="var(--blue-mid)" stroke-width="10" stroke-linecap="round"/>
  </svg>

  <!-- life insurance online -->
  <h2 class="abs h2" style="left:134px;top:905px">Life Insurance Online</h2>
  <p class="abs lede" style="left:136px;top:952px;width:340px">Compare quotes from America's top insurance carriers<br>Pick your policy and apply online in minutes.</p>
  <div class="btn" style="left:134px;top:1006px;width:170px">Get Your Quote</div>
  <div class="abs arch" style="left:820px;top:707px;width:320px;height:370px;background:linear-gradient(160deg,#8a8e84,#c9c6bc 60%,#e6e3dc)" role="img" aria-label="Photo of a smiling woman working on a laptop"></div>
  <div class="abs carrier-panel">
    <div class="carrier-panel__bar"><i></i><i></i><i></i></div>
    <div class="carrier-grid">
      <div class="carrier">Northvale</div>
      <div class="carrier">Keystone<br>Mutual</div>
      <div class="carrier">Stoneway</div>
      <div class="carrier">Brightpath</div>
      <div class="carrier">Meridian</div>
      <div class="carrier">Prairie<br>Mutual</div>
    </div>
  </div>

  <!-- compare and save -->
  <div class="abs arch" style="left:134px;top:1190px;width:383px;height:370px;border-radius:190px 190px 0 0;background:linear-gradient(150deg,#a89a86,#d5d9d6 50%,#e6ecea)" role="img" aria-label="Photo of a hand using a tablet showing charts"></div>
  <div class="quote-card" style="left:358px;top:1183px;background:var(--green-pale)">
    <span class="seal"></span>$2,000,000 Death Benefit<br>$20 Year Level Term
    <div class="price" style="color:var(--green)">$18.<small>08 / MO</small></div>
  </div>
  <div class="quote-card" style="left:62px;top:1358px;background:var(--blue-pale)">
    <span class="seal"></span>$2,000,000 Death Benefit<br>$20 Year Level Term
    <div class="price" style="color:var(--blue)">$21.<small>17 / MO</small></div>
  </div>
  <div class="quote-card" style="left:360px;top:1500px;background:var(--teal-pale)">
    <span class="seal"></span>$2,000,000 Death Benefit<br>$20 Year Level Term
    <div class="price">$23.<small>28 / MO</small></div>
  </div>
  <h2 class="abs h2" style="left:689px;top:1287px">Compare And Save</h2>
  <ul class="abs points" style="left:692px;top:1340px;width:380px">
    <li>Get Quotes without having to enter your contact information.</li>
    <li>Decide what's best for you without having to deal with pushy insurance agents.</li>
    <li>Virtual agent tools are available to help you choose what life insurance policy is best for you and your family.</li>
  </ul>
  <div class="btn" style="left:690px;top:1477px;width:196px">Compare Carriers</div>

  <!-- virtual agent -->
  <h2 class="abs h2" style="left:136px;top:1808px">Virtual Agent</h2>
  <ul class="abs points" style="left:136px;top:1860px;width:360px">
    <li>Our Virtual Agent Lumi can help you calculate how much death benefit you need.</li>
    <li>Lumi can help you figure out what type of Life Insurance is right for you and your family.</li>
    <li>Lumi can evaluate your health history and provide you with accurate quotes.</li>
  </ul>
  <div class="btn" style="left:136px;top:2023px;width:164px">Virtual Agent</div>
  <div class="abs" style="left:730px;top:2050px;width:356px;height:50px;border-radius:50%;background:var(--blue-mist)"></div>
  <div class="abs" style="left:756px;top:1900px;width:170px;height:180px;border-radius:14px;background:var(--blue)" role="img" aria-label="Illustration of a robot assistant beside a desk"></div>
  <div class="abs" style="left:930px;top:1760px;width:130px;height:300px;border-radius:16px;background:linear-gradient(180deg,var(--blue-mist),var(--blue-soft))"></div>
  <div class="abs" style="left:960px;top:1980px;width:100px;height:100px;border-radius:12px;background:var(--blue)"></div>
  <div class="abs circle" style="left:622px;top:1693px;width:256px;height:256px;background:linear-gradient(160deg,#d6d4cc,#9b8d80 70%,#6d4a45)" role="img" aria-label="Photo of a man typing on a laptop"></div>

  <!-- live agent -->
  <svg class="abs" style="left:165px;top:2220px" width="350" height="395" viewBox="0 0 350 395" role="img" aria-label="Photo of a customer support agent wearing a headset">
    <defs><linearGradient id="hexFill" x1="0" y1="0" x2="1" y2="1"><stop offset="0" stop-color="#8c8c8c"/><stop offset="1" stop-color="#d9d6d2"/></linearGradient></defs>
    <polygon points="175,6 342,100 342,295 175,389 8,295 8,100" fill="url(#hexFill)" stroke="#fff" stroke-width="8"/>
  </svg>
  <div class="abs" style="left:446px;top:2258px;width:118px;height:118px;border-radius:50%;background:var(--green-pale);border:6px solid var(--white);display:flex;flex-direction:column;align-items:center;justify-content:center;text-align:center;font-size:13px;font-weight:600;color:#222;line-height:17px">
    <span style="font-size:9px;color:var(--green);font-weight:500;margin-bottom:4px">Call Toll Free:</span>1-888-555-<br>0142
  </div>
  <div class="abs" style="left:118px;top:2448px;width:124px;height:124px;border-radius:50%;background:var(--blue);border:6px solid var(--white);display:flex;flex-direction:column;align-items:center;justify-content:center;text-align:center;font-size:13px;font-weight:500;color:var(--white);line-height:17px">
    <span style="font-size:9px;margin-bottom:4px">Email:</span>info@cover<br>lantern.com
  </div>
  <h2 class="abs h2" style="left:689px;top:2300px">Live Agent Support</h2>
  <ul class="abs points" style="left:690px;top:2352px;width:380px">
    <li>If you need a Live Agent, CoverLantern has you covered. Our CoverLantern Agents are not paid a commission. So if you have questions our agents have the answers that best suit your needs.</li>
  </ul>
  <div class="abs contact-line" style="left:712px;top:2449px">
    <svg width="16" height="16" viewBox="0 0 16 16"><path d="M3 1 L6 4 L4.5 6 C5.5 8.5 7.5 10.5 10 11.5 L12 10 L15 13 L13 15 C7 15 1 9 1 3 Z" fill="var(--green)"/></svg>
    <span>Call Toll Free: <b>1-888-555-0142</b></span>
  </div>
  <div class="abs contact-line" style="left:712px;top:2480px">
    <svg width="16" height="12" viewBox="0 0 16 12"><rect width="16" height="12" rx="1" fill="var(--green)"/><path d="M1 1 L8 7 L15 1" fill="none" stroke="#fff" stroke-width="1.4"/></svg>
    <span>Email: <b>info@coverlantern.com</b></span>
  </div>
  <div class="btn" style="left:689px;top:2529px;width:202px">Live Agent Support</div>

  <!-- apply online -->
  <h2 class="abs h2" style="left:136px;top:2830px">Apply Online</h2>
  <ul class="abs points" style="left:136px;top:2880px;width:360px">
    <li>Pick your policy and apply online in minutes.</li>
    <li>Secure Online Portal keeps your information safe and secure.</li>
    <li class="strong">24/7 access to your policy documents.</li>
  </ul>
  <div class="btn" style="left:136px;top:3010px;width:154px">Portal Login</div>
  <div class="abs arch" style="left:732px;top:2728px;width:326px;height:376px;border-radius:163px 163px 0 0;background:linear-gradient(160deg,#9a8468,#c9b297 50%,#e4d8c8)" role="img" aria-label="Photo of a family smiling at a laptop together"></div>
  <div class="abs" style="left:583px;top:2951px;width:210px;height:92px;border-radius:10px;background:var(--blue-pale);display:flex;align-items:center;gap:16px;padding-left:20px;font-size:16px;font-weight:500;color:var(--blue-mid);line-height:21px">
    <svg width="34" height="40" viewBox="0 0 34 40"><rect x="2" y="2" width="24" height="32" rx="3" fill="none" stroke="var(--blue-mid)" stroke-width="2.4"/><path d="M8 12 H20 M8 18 H20 M8 24 H15" stroke="var(--blue-mid)" stroke-width="2.2"/><path d="M20 36 L32 22" stroke="var(--blue-mid)" stroke-width="3"/></svg>
    <span>24/7 Access<br>Documents.</span>
  </div>

  <!-- compare quotes band -->
  <div class="abs" style="left:0;top:3200px;width:1200px;height:380px;background:linear-gradient(90deg,#6fa83a,#8BC53F 50%,#7fba3a)" role="img" aria-label="Green-toned photo of a smiling family"></div>
  <svg class="abs" style="left:0;top:3190px" width="1200" height="400" viewBox="0 0 1200 400">
    <path d="M0 0 H1200 V20 C900 -10 600 110 300 70 C180 55 80 40 0 60 Z" fill="var(--white)"/>
    <path d="M35 30 C150 85 330 95 540 55" fill="none" stroke="var(--blue)" stroke-width="10" stroke-linecap="round"/>
    <path d="M0 400 V360 C300 340 600 280 900 300 C1020 308 1120 330 1200 330 V400 Z" fill="var(--white)"/>
    <path d="M690 290 C830 255 1020 255 1130 300" fill="none" stroke="var(--blue)" stroke-width="10" stroke-linecap="round"/>
  </svg>
  <h2 class="abs" style="left:0;top:3322px;width:1200px;text-align:center;color:var(--white);font-size:32px;font-weight:500">Compare Quotes</h2>
  <p class="abs" style="left:0;top:3372px;width:1200px;text-align:center;color:var(--white);font-size:14px">See your CoverLantern Free-Quote in seconds. No Contact Info Needed.</p>
  <div class="btn btn--blue" style="left:526px;top:3408px;width:146px">Free Quotes</div>

  <!-- partners -->
  <h2 class="abs partners__title">OUR PARTNER</h2>
  <div class="abs" style="left:490px;top:3705px;width:1px;height:210px;background:#eee"></div>
  <div class="abs" style="left:712px;top:3705px;width:1px;height:210px;background:#eee"></div>
  <div class="abs" style="left:290px;top:3808px;width:620px;height:1px;background:#eee"></div>
  <div class="partner" style="left:283px;top:3705px">Northvale</div>
  <div class="partner" style="left:500px;top:3705px">Harborline</div>
  <div class="partner" style="left:722px;top:3705px">Crestfield Life</div>
  <div class="partner" style="left:283px;top:3815px">Meridian</div>
  <div class="partner" style="left:500px;top:3815px">Stoneway</div>
  <div class="partner" style="left:722px;top:3815px">Prairie Mutual</div>

  <!-- footer -->
  <svg class="abs" style="left:0;top:3950px" width="1200" height="491" viewBox="0 0 1200 491">
    <path d="M0 60 C300 160 700 120 1200 10 V491 H0 Z" fill="var(--green)"/>
    <path d="M0 90 C320 180 720 140 1200 40 V491 H0 Z" fill="var(--blue)"/>
    <path d="M55 70 C160 140 330 150 520 110" fill="none" stroke="var(--blue)" stroke-width="10" stroke-linecap="round"/>
    <path d="M0 110 C300 190 720 150 1200 60" fill="none" stroke="var(--white)" stroke-width="3" opacity=".25"/>
  </svg>
  <div class="abs brand" style="left:68px;top:4197px;color:var(--white);font-size:38px">CoverLantern</div>
  <div class="abs social" style="left:108px;top:4264px"><span></span><span></span><span></span><span></span></div>
  <div class="abs footer-col" style="left:337px;top:4150px">
    <h4>Life Insurance Products</h4>
    <ul><li>10 Year Level Team</li><li>15 Year Level Team</li><li>20 Year Level Team</li><li>30 Year Level Team</li><li>Lifetime Coverage</li></ul>
  </div>
  <div class="abs footer-col" style="left:611px;top:4150px">
    <h4>Tools</h4>
    <ul><li>Quote Comparison</li><li>Secure Client portal</li><li>Privacy Policy</li></ul>
  </div>
  <div class="abs footer-col" style="left:888px;top:4150px"><h4>Contact</h4></div>
  <div class="abs footer-contact" style="left:886px;top:4190px">
    <div><svg width="16" height="12" viewBox="0 0 16 12"><rect width="16" height="12" rx="1" fill="var(--green)"/><path d="M1 1 L8 7 L15 1" fill="none" stroke="var(--blue)" stroke-width="1.4"/></svg>info@CoverLantern.com</div>
    <div><svg width="16" height="16" viewBox="0 0 16 16"><path d="M3 1 L6 4 L4.5 6 C5.5 8.5 7.5 10.5 10 11.5 L12 10 L15 13 L13 15 C7 15 1 9 1 3 Z" fill="var(--green)"/></svg>1-888-555-0142</div>
    <div><svg width="16" height="16" viewBox="0 0 16 16"><circle cx="8" cy="8" r="7" fill="none" stroke="var(--green)" stroke-width="1.6"/><path d="M8 4 V8 L11 10" fill="none" stroke="var(--green)" stroke-width="1.6"/></svg><span>Monday - Friday<br>9:00AM - 8:00PM</span></div>
    <div><svg width="16" height="22" viewBox="0 0 16 22"><path d="M8 1 C4 1 1 4 1 8 C1 13 8 21 8 21 C8 21 15 13 15 8 C15 4 12 1 8 1 Z" fill="none" stroke="var(--green)" stroke-width="1.6"/><circle cx="8" cy="8" r="2.5" fill="var(--green)"/></svg><span>4200 HARBOR LANE,<br>SUITE 110 LAKEVIEW, FL<br>30000</span></div>
  </div>
  <p class="abs copyright">©CoverLantern - 2022 All rights reserved.</p>

</div>
</body>
</html>
```